Desert Basin Company Brochure

**** UPDATE 2-8-2014 ****

Size should be 11" X 17" or larger (tri or bi fold).

We're going to let the contest run it's full duration to allow for more time spent on designs.

No black backgrounds.

Consideration should be given to having the text be easy to read and in a nice, organized format.

*****************************

We're looking for an eye-catching, colorful brochure that will explain what we do, who we are... and what sets us apart from the competition.

Our company provides swimming pool service, repair, and custom renovations throughout the Phoenix, Arizona metropolitan area. These brochures will be hand-delivered to each prospective customer we visit.

The brochure will include images of our work, product logos, and a unique design that separates our company apart from the rest.

The brochure should be tri-fold. Although, if a designer wants to (or has better ideas) for a different lay-out, then we're open to seeing what can be done.

Colors we like: Blue, White, Silver, Copper, Green (accent color)

We like designs that are unique/different. Professional. Creative. Sleek. Sexy. Custom. We don't want the brochure to be "pretentious". We'd like for these brochures to leave a lasting impression with our prospective clients... and hopefully earn us more business.

We don't want the brochure to be too wordy, however if the designer feels we need to cut back (or add), let us know.

Our motto is "Every Ripple Counts Twice".

You can view some of our projects, and what we're about either at our website (brightwaveaqua.example), Chatterbook (www.facebook/brightwaveaqua), or Searchly+ (https://plus.google.com/+Brightwaveaqua). Thank you!

- Print-

(Front) Logo

Service - Repair - Renovation
555-731-4409
brightwaveaqua.example
service@brightwaveaqua.example
Like Us On Chatterbook! Chatterbook LOGO
Searchly Plus LOGO

(Body) Why Choose Us?

Thank you for the opportunity for our company to become your pool service provider!

We’re committed to providing the best customer service possible! At the end of the day you want your pool to be clean, clear, operational, and for your service provider to be available when you need them!

We’re licensed with the Westland Board Of Tradesmen, Bonded, and Fully Insured.
A+ reviews with the Honest Trade Council, Marla’s Picks, Wombit, Vyn, Chatterbook, and Searchly!
All technicians are employees... not sub-contractors! Our employees are hard working, dependable, professional, and expected to follow our strict protocol for servicing your pool.
Flat-fee service rates! Any additional equipment repairs, maintenance, or chemical implementations are directly authorized by you!
No contracts! Our Service Level Agreement Form allows you to select your desired level of authorization for equipment repairs, filter maintenance, and extra chemical implementation programs.
Our uniformed technicians arrive in distinctive, clean GPS-tracked company trucks.
We leave detailed service slips after each service visit. In addition, all service visit information is electronically recorded and stored.
Easy, online account management to view and pay invoices or authorize estimates.
Invoices, estimates, questions, pictures, and video are communicated via e-mail!
Free service calls to diagnose equipment issues outside of our normal service.
10% Service Client Discount for all repairs and replacement items.
Brightwave Aqua knows the importance of communication! We’re available by phone, email, or text all days of the week.

(Body) Our Methodology

We believe in 5 important factors in maintaining a clean, clear, and operational pool...

Good, Clean Water! Our local water supply contains high amounts of minerals. Pool chemicals add to this problem in a short amount of time. Our philosophy is to use the least amount of chemicals possible to achieve optimal water balance.
Efficient Water Flow! The invention of variable-speed pumps has enabled the ability to "dial in" proper water flow... while driving down energy costs.
Proper Filtration! Today’s high-capacity cartridge filters provide great filtration, save on wasted water from backwashing sand filters, and eliminate the need for water flow-restricting backwash valves.
Functioning Cleaning System! Having a working automatic cleaning system is vital in keeping the pool surface clean of debris and dirt... and free of staining.
A Dependable And Professional Pool Maintenance Technician! Our job is to not only oversee all of the items listed above... but to make sure your pool is in the best condition possible!

(Body) Equipment Repair & Installation

We’re educated on all phases of swimming pool equipment repair and installation... with a focus on energy-efficiency and optimum performance!

We’re an KTV & MWE Authorized Installer of variable-speed pool pumps. KTV & MWE trust us to properly install and calibrate all variable-speed pumps. We've been equipped to handle the new industry standards on variable-speed pumps since Arizona law went into effect January 1st, 2011.
We’re experts at acid washes and erasing the mineral build-up off of waterlines. All work is done in-house with our customized cleaning rig and trailer.
Heating systems. New efficiency standards have made installation and operation more affordable than ever.
Remote control automation systems. Technology now allows the user to easily view and control their entire pool system via a remote home computer, tablet, or phone!
Brilliant, color-changing LED lighting for pools and spas! The benefits of LED include brighter and broader displays... while lasting much longer than your typical light bulbs.
Salt systems provide a soft-water experience! In addition to the benefit of better feeling water, salt systems generate plenty of chlorine to keep your pool sanitized.

(Body) About Us

A native to Phoenix, Dorian Kessel founded Brightwave Aqua in 2000. Our company was built from the ground up by way of hard work, word of mouth, and determination. Our company will always remain firmly grounded, and continue to develop systems that put our customers first!

Our philosophy is to treat every pool as if it were our own, run an efficient and organized business, and care for our employees.

Brightwave Aqua is a yearly, proud contributor to the Saguaro Youth Medical Center Splash Smart Day. Please educate and watch all children around water... every accident can be avoided.

(Back) Contact Us
Logos To Use, Files Uploaded: Marla’s Picks, HTC, Hydrova, Searchly+, Chatterbook, KTV/MWE logo, Saguaro Youth Medical Center

Office: 555-731-4409 | Fax: 555-731-4413 | Email: service@brightwaveaqua.example
brightwaveaqua.example

Office / Warehouse Location
41276 East Cholla Street, Suite 8
Phoenix, Arizona 85999
(NW of Cholla Street & Ironwood Mesa Road)

AZ ROC: 731502, 731503, 731504, 864017

Target Market(s)

We target a market of pool owners, which typically have more disposable income.

30 - 75 years old.

Our clients range from first-time home buyers, self-employed, business professionals, doctors, landlords, thousandaires, millionaires.

Industry/Entity Type

Pool Service

Font styles to use
Serif

Colors
0355a3
cfdfed
ffffff
3176b5
eaf1f7

Requirements
Must have
• Must use provided images. We've included a few pool pictures, and will let you decide which ones to incorporate throughout the brochure.

Logos Used:
Brightwave Aqua
Hydrova
HTC
Marla's Picks
KTV
MWE
Saguaro Youth Medical Center
Searchly+
Chatterbook

Image pic of some of our trucks.

Nice to have
• Equipment images worked in.
Should not have
• Cartoonish fonts or design. No "Love" hearts!!

```html
<!DOCTYPE html>
<html lang="en">
<head>
<meta charset="utf-8">
<title>Desert Basin Company Brochure</title>
<link rel="stylesheet" href="https://fonts.googleapis.com/css2?family=Arimo:wght@400;700&display=swap">
<style>
:root{
  --navy:#1b2f8c;
  --royal:#2746b4;
  --sky:#a9c4ea;
  --pale:#eaf1f7;
  --green:#8cc63f;
  --white:#ffffff;
  --brand:#1f3fa8;
  --red:#d6262c;
  --ink:#2b3a55;
}
*{box-sizing:border-box;margin:0;padding:0}
html,body{width:772px;height:1200px;overflow:hidden;background:var(--white)}
body{font-family:"Arimo",Arial,sans-serif;color:var(--white)}
.brochure{position:relative;width:772px;height:1200px}
.panel{position:absolute;left:0;width:772px;overflow:hidden}
.outside{top:0;height:590px;background:var(--navy)}
.inside{top:598px;height:602px;background:var(--royal)}
.layer{position:absolute;left:0;top:0}
.abs{position:absolute}

/* partner names */
.partner{position:absolute;font-weight:700;font-size:17px;letter-spacing:.5px}
.partner-mwe{left:304px;top:22px;color:var(--red)}
.partner-ktv{left:400px;top:22px;color:var(--ink)}
.partner-ktv::before{content:"";display:inline-block;width:14px;height:14px;border-radius:50%;background:#2c8fd6;margin-right:5px;vertical-align:-2px}
.partner-hospital{left:298px;top:56px;width:90px;font-size:9px;line-height:11px;color:var(--red)}
.partner-hydrova{left:392px;top:60px;font-size:15px;color:var(--ink);letter-spacing:1px}
.badge-listing{left:312px;top:96px;width:46px;height:46px;border-radius:50%;background:#7fb23a}
.badge-trade{left:418px;top:100px;width:36px;height:50px;background:#22407a;border-radius:3px}

.client-logo{left:528px;top:44px;width:236px;text-align:center;color:var(--brand)}
.client-logo .mark{display:inline-block;width:30px;height:30px;border-radius:50%;background:var(--brand);vertical-align:middle;margin-right:6px}
.client-logo .name{font-size:28px;font-weight:700;vertical-align:middle;letter-spacing:-.5px}
.client-logo .motto{display:block;font-size:11px;font-weight:700;margin-top:2px;padding-left:60px}

.about{left:14px;top:248px;width:226px}
.about h2{font-size:19px;text-align:center;margin-bottom:10px}
.about p{font-size:12px;line-height:14.4px;margin-bottom:14px}

.contact{left:264px;top:359px;width:228px;text-align:center;font-size:12px;line-height:14.4px}
.contact .label{color:var(--green);font-weight:700}
.contact .block{margin-bottom:14px}
.contact .social{font-size:14px;line-height:18px;margin-top:18px}
.icon-sq{display:inline-block;width:14px;height:14px;vertical-align:-2px;margin-left:4px}
.icon-fb{background:#3b5ba8;border:1px solid var(--white)}
.icon-sp{background:#d6402f}

.service{left:528px;top:506px;width:240px;text-align:center;font-size:13px;line-height:15.5px}
.service h3{color:var(--green);font-size:16px;font-weight:700;margin-bottom:2px}
.service .phone{font-weight:700}

/* inside */
.why{left:0;top:0;width:256px;height:602px;background:var(--navy);padding:26px 10px 0 12px}
.why h2{font-size:19px;margin-bottom:9px}
.why p{font-size:10.4px;line-height:12.6px;margin-bottom:10.4px}

.method{left:262px;top:248px;width:254px}
.method h2{font-size:17px;margin-bottom:4px}
.method h4{color:var(--green);font-size:11.4px;font-weight:700;line-height:13px}
.method p{font-size:10.4px;line-height:12.4px;margin-bottom:4px}

.equip{left:523px;top:254px;width:244px}
.equip h2{font-size:17px;line-height:20px;margin-bottom:18px}
.equip p{color:var(--green);font-weight:700;font-size:11.4px;line-height:13.6px;margin-bottom:13px}
</style>
</head>
<body>
<main class="brochure">

  <!-- Outside panel -->
  <section class="panel outside">
    <svg class="layer" width="772" height="590" viewBox="0 0 772 590" aria-hidden="true">
      <path d="M0 0H772V150C640 170 560 250 420 240C300 230 200 160 0 210Z" fill="var(--sky)"/>
      <path d="M0 0H772V128C630 140 540 220 400 212C270 204 170 140 0 180Z" fill="var(--white)"/>
    </svg>
    <svg class="layer" width="252" height="160" viewBox="0 0 252 160" role="img" aria-label="Photo of stone steps leading into a pool">
      <defs><linearGradient id="g1" x1="0" y1="0" x2="1" y2="1"><stop offset="0" stop-color="#c9b79a"/><stop offset=".45" stop-color="#5f7fa8"/><stop offset="1" stop-color="#1f3f88"/></linearGradient></defs>
      <path d="M0 0H252V118C180 118 90 140 0 160Z" fill="url(#g1)"/>
    </svg>
    <svg class="layer" width="772" height="430" viewBox="0 0 772 430" role="img" aria-label="Photo of a backyard pool with palms at dusk">
      <defs><linearGradient id="g2" x1="0" y1="0" x2="0" y2="1"><stop offset="0" stop-color="#dfe9f4"/><stop offset=".35" stop-color="#4c7a3c"/><stop offset=".65" stop-color="#2a7fc4"/><stop offset="1" stop-color="#c9b48d"/></linearGradient></defs>
      <path d="M516 236C600 200 680 160 772 130V420H640C600 380 560 300 516 236Z" fill="url(#g2)"/>
      <path d="M516 236C600 200 680 160 772 130" stroke="var(--green)" stroke-width="4" fill="none"/>
    </svg>

    <span class="partner partner-mwe">MWE</span>
    <span class="partner partner-ktv">KTV</span>
    <span class="partner partner-hospital">Saguaro Youth Medical Center</span>
    <span class="partner partner-hydrova">HYDROVA</span>
    <span class="abs badge-listing" aria-hidden="true"></span>
    <span class="abs badge-trade" aria-hidden="true"></span>

    <div class="abs client-logo">
      <span class="mark"></span><span class="name">brightwaveaqua</span>
      <span class="motto">every ripple counts twice</span>
    </div>

    <div class="abs about">
      <h2>About Us</h2>
      <p>A native to Phoenix, Dorian Kessel founded Brightwave Aqua in 2000. Our company was built from the ground up by way of hard work, word of mouth, and determination. Our company will always remain firmly grounded, and continue to develop systems that put our customers first!</p>
      <p>Our philosophy is to treat every pool as if it were our own, run an efficient and organized business, and care for our employees.</p>
      <p>Brightwave Aqua is a yearly, proud contributor to the Saguaro Youth Medical Center Splash Smart Day. Please educate and watch all children around water... every accident can be avoided.</p>
    </div>

    <div class="abs contact">
      <div class="block">
        <div class="label">O: 555-731-4409</div>
        <div class="label">F: 555-731-4413</div>
        <div>service@brightwaveaqua.example</div>
      </div>
      <div class="block">
        <div class="label">Office / Warehouse Location:</div>
        <div>41276 East Cholla Street, Suite 8</div>
        <div>Phoenix, Arizona 85999</div>
        <div>(NW of Cholla Street &amp; Ironwood Mesa Road)</div>
      </div>
      <div>AZ ROC: 731502, 731503, 731504, 864017</div>
      <div class="social">
        <div>Like Us On Chatterbook!<span class="icon-sq icon-fb"></span></div>
        <div>Searchly Plus<span class="icon-sq icon-sp"></span></div>
      </div>
    </div>

    <div class="abs service">
      <h3>Service - Repair - Renovation</h3>
      <div class="phone">555-731-4409</div>
      <div>service@brightwaveaqua.example</div>
      <div>www.brightwaveaqua.example</div>
    </div>
  </section>

  <!-- Inside panel -->
  <section class="panel inside">
    <svg class="layer" width="772" height="602" viewBox="0 0 772 602" role="img" aria-label="Photo of a pool and spa with rock waterfall and pink flowers">
      <defs><linearGradient id="g3" x1="0" y1="0" x2="1" y2="1"><stop offset="0" stop-color="#9c8a6e"/><stop offset=".35" stop-color="#d77aa8"/><stop offset=".55" stop-color="#3fa6d8"/><stop offset="1" stop-color="#7cc6e6"/></linearGradient></defs>
      <rect x="256" y="0" width="516" height="250" fill="url(#g3)"/>
      <path d="M256 232C420 260 600 200 772 150V250H256Z" fill="var(--white)"/>
      <path d="M256 232C420 260 600 200 772 150" stroke="var(--green)" stroke-width="5" fill="none"/>
      <path d="M256 252C440 270 620 220 772 180V602H256Z" fill="var(--royal)"/>
    </svg>

    <div class="abs why">
      <h2>Why Choose Us?</h2>
      <p>We’re licensed with the Westland Board Of Tradesmen, Bonded, and Fully Insured.</p>
      <p>A+ reviews with the Honest Trade Council, Marla’s Picks, Wombit, Vyn, Chatterbook, and Searchly!</p>
      <p>All technicians are employees... not sub-contractors! Our employees are hard working, dependable, professional, and expected to follow our strict protocol for servicing your pool.</p>
      <p>Flat-fee service rates! Any additional equipment repairs, maintenance, or chemical implementations are directly authorized by you!</p>
      <p>No contracts! Our Service Level Agreement Form allows you to select your desired level of authorization for equipment repairs, filter maintenance, and extra chemical implementation programs.</p>
      <p>Our uniformed technicians arrive in distinctive, clean GPS-tracked company trucks.</p>
      <p>We leave detailed service slips after each service visit. In addition, all service visit information is electronically recorded and stored.</p>
      <p>Easy, online account management to view and pay invoices or authorize estimates.</p>
      <p>Invoices, estimates, questions, pictures, and video are communicated via e-mail!</p>
      <p>Free service calls to diagnose equipment issues outside of our normal service.</p>
      <p>10% Service Client Discount for all repairs and replacement items.</p>
      <p>Brightwave Aqua knows the importance of communication! We’re available by phone, email, or text all days of the week.</p>
    </div>

    <div class="abs method">
      <h2>Our Methodology</h2>
      <h4>Good, Clean Water</h4>
      <p>Our local water supply contains high amounts of minerals. Pool chemicals add to this problem in a short amount of time. Our philosophy is to use the least amount of chemicals possible to achieve optimal water balance.</p>
      <h4>Efficient Water Flow</h4>
      <p>The invention of variable-speed pumps has enabled the ability to "dial in" proper water flow... while driving down energy costs.</p>
      <h4>Proper Filtration</h4>
      <p>Today’s high-capacity cartridge filters provide great filtration, save on wasted water from backwashing sand filters, and eliminate the need for water flow-restricting backwash valves.</p>
      <h4>Functioning Cleaning System</h4>
      <p>Having a working automatic cleaning system is vital in keeping the pool surface clean of debris and dirt... and free of staining.</p>
      <h4>A Dependable And Professional Pool Maintenance Technician</h4>
      <p>Our job is to not only oversee all of the items listed above... but to make sure your pool is in the best condition possible!</p>
    </div>

    <div class="abs equip">
      <h2>Equipment Repair<br>and Installation</h2>
      <p>We’re an KTV &amp; MWE Authorized Installer of variable-speed pool pumps.</p>
      <p>We’re experts at acid washes and erasing the mineral build-up off of waterlines.</p>
      <p>Heating systems.</p>
      <p>Remote control automation systems.</p>
      <p>Brilliant, color-changing LED lighting for pools and spas!</p>
      <p>Salt systems provide a soft-water experience!</p>
    </div>
  </section>

</main>
</body>
</html>
```